brolvin business card design so that it looks better

need a new business card designed. use our website, brolvix.example for example. I attached an example of a previous card we had and liked. this is for law enforcement and we have attached a previous business card as an example. This site forces me to select color and font, ignore those as I picked stuff just to get this completed.

Target Market(s)

law enforcement, local government

Contact Information for Business Card

see the attached example and our website

Font styles to use
Serif

```html
<!DOCTYPE html>
<html lang="en">
<head>
<meta charset="UTF-8">
<title>Brolvin Business Card</title>
<link href="https://fonts.googleapis.com/css2?family=Arimo:wght@400;700&display=swap" rel="stylesheet">
<style>
  :root {
    --page-bg: #d9d4cc;
    --card-light: #f1f2f3;
    --card-mid: #dfe2e5;
    --panel-dark: #15181c;
    --panel-edge: #2c3136;
    --accent-blue: #1f4f9c;
    --ink-dark: #1d2125;
    --ink-blue: #2a5aa8;
  }
  * { margin: 0; padding: 0; box-sizing: border-box; }
  html, body {
    width: 1200px;
    height: 970px;
    overflow: hidden;
    background: var(--page-bg);
  }
  .card {
    position: absolute;
    left: 80px;
    top: 188px;
    width: 1040px;
    height: 594px;
    border-radius: 30px;
    overflow: hidden;
    background: linear-gradient(160deg, var(--card-light) 0%, var(--card-mid) 100%);
    box-shadow: 0 14px 40px rgba(0,0,0,0.22);
    font-family: "Arimo", Arial, sans-serif;
  }
  .card-art {
    position: absolute;
    inset: 0;
  }
  .brand-name {
    position: absolute;
    left: 56px;
    top: 78px;
    font-size: 104px;
    font-weight: 700;
    letter-spacing: 4px;
    line-height: 1;
    color: var(--ink-dark);
  }
  .person {
    position: absolute;
    left: 58px;
    top: 292px;
  }
  .person-name {
    font-size: 34px;
    font-weight: 700;
    color: var(--ink-dark);
    line-height: 1;
  }
  .person-title {
    margin-top: 4px;
    font-size: 26px;
    color: var(--ink-blue);
    line-height: 1;
  }
  .address {
    position: absolute;
    left: 58px;
    top: 378px;
    font-size: 26px;
    line-height: 31px;
    color: var(--ink-dark);
  }
  .contacts {
    position: absolute;
    left: 58px;
    top: 456px;
    list-style: none;
  }
  .contact-item {
    display: flex;
    align-items: center;
    height: 33px;
    font-size: 26px;
    color: var(--ink-dark);
  }
  .contact-item svg {
    width: 22px;
    height: 22px;
    margin-right: 16px;
    flex: none;
  }
  .contact-web { letter-spacing: 2px; }
</style>
</head>
<body>
  <div class="card">
    <svg class="card-art" viewBox="0 0 1040 594" aria-hidden="true">
      <defs>
        <linearGradient id="panelShade" x1="0" y1="0" x2="1" y2="1">
          <stop offset="0" stop-color="var(--panel-edge)"/>
          <stop offset="1" stop-color="var(--panel-dark)"/>
        </linearGradient>
      </defs>
      <path d="M665,0 Q870,70 927,300 Q900,115 822,0 Z" fill="var(--accent-blue)"/>
      <path d="M845,0 Q1018,343 840,594 L1040,594 L1040,0 Z" fill="url(#panelShade)"/>
      <path d="M836,0 Q1010,343 831,594" fill="none" stroke="#ffffff" stroke-width="4"/>
    </svg>

    <div class="brand-name">BROLVIN</div>

    <div class="person">
      <div class="person-name">DANA WHITLOCK</div>
      <div class="person-title">Director</div>
    </div>

    <div class="address">
      4128 Brightmoor Lane<br>
      Calloway, TX 70412
    </div>

    <ul class="contacts">
      <li class="contact-item">
        <svg viewBox="0 0 24 24"><path d="M7 2 L10 7 L8 9 Q9 14 14 17 L16 15 L21 18 L19 22 Q8 21 3 6 Z" fill="var(--ink-blue)"/></svg>
        555.014.2273
      </li>
      <li class="contact-item">
        <svg viewBox="0 0 24 24"><rect x="2" y="5" width="20" height="14" fill="var(--ink-blue)"/><path d="M2 5 L12 13 L22 5" fill="none" stroke="#ffffff" stroke-width="1.6"/></svg>
        info@brolvix.example
      </li>
      <li class="contact-item contact-web">
        <svg viewBox="0 0 24 24"><circle cx="12" cy="12" r="10" fill="var(--ink-blue)"/><g fill="none" stroke="#ffffff" stroke-width="1.2"><ellipse cx="12" cy="12" rx="4.5" ry="10"/><line x1="2" y1="12" x2="22" y2="12"/><line x1="4" y1="7" x2="20" y2="7"/><line x1="4" y1="17" x2="20" y2="17"/></g></svg>
        www.brolvix.example
      </li>
    </ul>
  </div>
</body>
</html>
```